Automotive Mechanic Website Design

We are working with an auto repair shop in California.
A few websites for inspiration:
https://brindlecovemotors.example
https://www.folionest.example/gallery/57316284/Torvane-Auto-Services-Repair-SiteKit-Theme
http://www.quelbrightmotors.example
https://www.halvikgarage.example
https://www.pdmotorhaus.example
Thank you for taking the time to consider designing a website for us. We are web developers based in Stockton, CA, USA. Most of our projects go through the same process. Understanding this process may help you win a project with us. We custom-code all of our websites in-house. We don’t have any requirements as to what tools you use for your design, but we ask that you follow these guidelines.
IMAGES:
If you use any images or icons in the design, we ask that you have a link to the asset so we can purchase the image/icon. Most of the designs we submit do not have the customer’s images on them unless they have some great images. Be creative; show us the feeling you are trying to portray with your image choices. Use any royalty-free site you choose. We subscribe to Adobe and mainly use their images, but we can purchase images outside of Adobe. PLEASE NOTE: we will not submit designs to clients with watermarks on the images.
FONTS:
We ask that you identify the fonts you’re using in the design. This can be done in a message if you want. We typically use Google Fonts and Adobe Fonts.
CONTENT:
We're always open to different content and ideas. We often submit designs with stock images so the client can see our vision. We typically take pictures after the website launch to use their images with our vision. Lorem Ipsum is fine for paragraphs, but we ask that you make the Headers with correct English. We want to be able to show the vision and identify the sections of the website.
INSPIRATION:
We typically add a couple of links in the brief of websites we like to help you get started in your design.
REVISIONS:
We do not often ask for revisions of the designs unless we see something in the design that may not appeal to the client. If there are slight changes that we want to make, we do that in the development process.
FEEDBACK:
We rarely give feedback on designs during the design process. We are working on many website projects and do not have the time to provide feedback. We usually respond if your request is well thought out and asks specific questions, but a note asking “feedback, please” usually goes unanswered.

```html
<!DOCTYPE html>
<html lang="en">
<head>
<meta charset="utf-8">
<title>Kestrel Auto Repair</title>
<link href="https://fonts.googleapis.com/css2?family=Russo+One&family=Raleway:wght@400;500;600&display=swap" rel="stylesheet">
<style>
:root{
  --red:#ee2a35;
  --ink:#161616;
  --dark:#222222;
  --black:#0d0d0d;
  --grey:#555;
  --light:#f4f4f4;
  --white:#fff;
}
*{box-sizing:border-box;margin:0;padding:0}
html,body{width:1200px;height:3075px;overflow:hidden}
body{position:relative;background:var(--white);font-family:"Raleway",sans-serif;color:var(--ink)}
.abs{position:absolute}
.display{font-family:"Russo One",sans-serif;text-transform:uppercase}
.ph{position:absolute}
.btn{position:absolute;display:flex;align-items:center;justify-content:center;font-family:"Russo One",sans-serif;font-size:15px;text-transform:uppercase}
.btn-outline-red{border:2px solid var(--red);color:var(--red);background:var(--white)}
.btn-outline-white{border:2px solid var(--white);color:var(--white)}
/* header */
.logo{font-family:"Russo One",sans-serif;color:var(--red);line-height:1}
.logo .word{font-size:50px;letter-spacing:2px}
.logo .sub{font-size:20px;color:var(--ink);text-align:right;margin-top:-4px}
.nav{left:435px;top:40px;display:flex;gap:47px;font-size:16px}
.quote{left:952px;top:26px;width:136px;height:50px;background:var(--red);color:var(--white)}
/* hero */
.hero-mark{left:30px;top:150px;font-family:"Russo One",sans-serif;font-size:190px;color:#eeeeee;letter-spacing:6px;line-height:1}
.hero-title{left:112px;top:262px;font-size:50px;line-height:70px;color:var(--ink)}
/* tiles */
.tile{position:absolute;top:630px;width:300px;height:300px;overflow:hidden}
.tile h3{position:absolute;left:25px;top:63px;color:var(--white);font-family:"Russo One",sans-serif;font-size:24px;line-height:35px;text-transform:uppercase}
.tile .num{position:absolute;right:15px;bottom:-40px;font-family:"Russo One",sans-serif;font-size:170px;color:rgba(255,255,255,.12);line-height:1}
.tile .btn{left:25px;top:186px;width:129px;height:50px}
/* about */
.about-h{left:665px;top:1020px;font-size:40px}
.about-p{left:665px;top:1100px;width:395px;font-size:15px;line-height:25.7px;color:var(--grey)}
/* blog */
.blog{left:0;top:1510px;width:1200px;height:685px;background:var(--dark)}
.blog-title{left:0;top:1610px;width:1200px;text-align:center;color:var(--white);font-size:38px}
.card{left:157px;top:1925px;width:491px;height:160px;background:var(--white);padding:30px 34px}
.card h4,.side h4{font-family:"Russo One",sans-serif;font-size:19px;text-transform:uppercase}
.card p{font-size:14px;line-height:24px;color:var(--grey);margin-top:4px}
.more{display:inline-block;margin-top:8px;font-family:"Russo One",sans-serif;font-size:15px;color:var(--red);text-decoration:underline;text-transform:uppercase}
.side{left:865px;width:245px;color:var(--white)}
.side p{font-size:14px;line-height:24px;color:#ccc;margin-top:4px}
/* makes */
.makes-title{left:0;top:2275px;width:1200px;text-align:center;font-size:38px}
.make{position:absolute;width:126px;height:70px;display:flex;align-items:center;justify-content:center}
.make.active{background:var(--white);box-shadow:0 4px 16px rgba(0,0,0,.1);border-radius:4px}
/* footer */
.footer{left:0;top:2715px;width:1200px;height:360px;background:var(--black);color:var(--white)}
.social{position:absolute;top:2900px;width:38px;height:38px;border-radius:50%;background:var(--red)}
.social.alt{background:var(--white)}
.fcol{position:absolute;top:2780px}
.fcol h5{font-size:21px;font-weight:600;margin-bottom:12px}
.fcol li{list-style:none;font-size:16px;line-height:26px;padding-left:25px;position:relative}
.fcol li.arrow::before{content:"»";position:absolute;left:0;top:-1px}
.contact-row{display:flex;gap:10px;font-size:16px;line-height:26px;margin-bottom:16px}
</style>
</head>
<body>

<!-- header -->
<div class="abs logo" style="left:112px;top:18px"><div class="word">KESTREL</div><div class="sub">AUTO REPAIR</div></div>
<nav class="abs nav"><span>Home</span><span>About</span><span>Services</span><span>Blog</span><span>Contact</span></nav>
<svg class="abs" style="left:896px;top:42px" width="18" height="18" viewBox="0 0 18 18"><circle cx="7.5" cy="7.5" r="5.5" fill="none" stroke="#ee2a35" stroke-width="2.6"/><line x1="11.5" y1="11.5" x2="16" y2="16" stroke="#ee2a35" stroke-width="2.8" stroke-linecap="round"/></svg>
<div class="btn quote">Get a Quote</div>

<!-- hero -->
<div class="abs hero-mark">KESTREL</div>
<h1 class="abs hero-title display">Auto Repair Shop<br>in California</h1>
<div class="btn btn-outline-red" style="left:112px;top:428px;width:136px;height:50px">Learn More</div>
<div class="ph" role="img" aria-label="Red sedan car, front three-quarter view" style="left:612px;top:188px;width:588px;height:355px;background:radial-gradient(ellipse at 45% 55%,#d9232c 0%,#a5161d 55%,rgba(255,255,255,0) 72%)"></div>

<!-- service tiles -->
<div class="tile" style="left:0;background:var(--red)">
  <h3>Maintenance<br>Services</h3><div class="num">01</div>
  <div class="btn btn-outline-white">Start Now</div>
</div>
<div class="tile" role="img" aria-label="Mechanic working on an engine" style="left:300px;background:linear-gradient(135deg,#6a6e72,#2b2d30)"></div>
<div class="tile" style="left:600px;background:var(--dark)">
  <h3>Certified Repair<br>Services</h3><div class="num">02</div>
  <div class="btn btn-outline-white">Start Now</div>
</div>
<div class="tile" role="img" aria-label="Hand signing a service document beside a model car" style="left:900px;background:linear-gradient(135deg,#e6e7ea,#9ba2ab)"></div>

<!-- about -->
<div class="ph" role="img" aria-label="Gloved hand tightening an engine part" style="left:115px;top:1045px;width:207px;height:380px;background:linear-gradient(160deg,#7b8088,#24272b)"></div>
<div class="ph" role="img" aria-label="Mechanic in blue overalls holding a tablet in the workshop" style="left:345px;top:1020px;width:208px;height:380px;background:linear-gradient(170deg,#b0503e,#4a6aa0 55%,#2c3f66)"></div>
<h2 class="abs about-h display">About Kestrel</h2>
<p class="abs about-p">Lorem ipsum dolor sit amet, consectetur adipiscing elit, sed do eiusmod tempor incididunt ut labore et dolore magna aliqua. Ut enim ad minim veniam, quis nostrud exercitation ullamco laboris nisi ut aliquip ex ea commodo consequat. Duis aute irure dolor in reprehenderit in voluptate velit esse cillum dolore eu t non proident, sunt in culpa qui officia deserunt mollit anim id est laborum.</p>
<div class="btn btn-outline-red" style="left:665px;top:1342px;width:136px;height:50px">Learn More</div>

<!-- blog -->
<div class="abs blog"></div>
<h2 class="abs blog-title display">Latest Blog</h2>
<div class="ph" role="img" aria-label="Mechanic inspecting a wheel under a lifted car" style="left:112px;top:1715px;width:518px;height:355px;background:linear-gradient(135deg,#8a9096,#3b4045)"></div>
<div class="abs card">
  <h4>Lorem ipsum dolor sit amet, consectetur elit,</h4>
  <p>sed do eiusmod tempor incididunt ut labore et dolore magna aliqua. Quis ipsum suspendisse ultrices gravida.</p>
  <span class="more">Read More</span>
</div>
<div class="ph" role="img" aria-label="Mechanic holding wrenches in front of a car" style="left:682px;top:1715px;width:164px;height:160px;background:linear-gradient(135deg,#b9bec4,#2c3440)"></div>
<div class="abs side" style="top:1718px">
  <h4>Lorem ipsum dolor amet,</h4>
  <p>sed do eiusmod incididunt ut labore et dolore magna aliqua. Quis ipsum suspendisse ultrices gravida.</p>
  <span class="more">Read More</span>
</div>
<div class="ph" role="img" aria-label="Man polishing a car headlight with a yellow cloth" style="left:682px;top:1917px;width:164px;height:168px;background:linear-gradient(135deg,#a89a80,#2e3136)"></div>
<div class="abs side" style="top:1920px">
  <h4>Lorem ipsum dolor amet,</h4>
  <p>sed do eiusmod incididunt ut labore et dolore magna aliqua. Quis ipsum suspendisse ultrices gravida.</p>
  <span class="more">Read More</span>
</div>

<!-- makes -->
<h2 class="abs makes-title display">We Service Most Makes and Models</h2>
<div class="make" style="left:232px;top:2365px"><svg width="60" height="30"><rect x="2" y="5" width="56" height="20" rx="4" fill="#ddd"/></svg></div>
<div class="make" style="left:360px;top:2365px"><svg width="44" height="36"><rect x="4" y="3" width="36" height="30" rx="7" fill="none" stroke="#ccc" stroke-width="3"/></svg></div>
<div class="make" style="left:482px;top:2365px"><svg width="56" height="32"><ellipse cx="28" cy="16" rx="25" ry="13" fill="none" stroke="#ccc" stroke-width="3"/></svg></div>
<div class="make active" style="left:612px;top:2365px"><svg width="46" height="46"><circle cx="23" cy="23" r="20" fill="none" stroke="#ee2a35" stroke-width="3.5"/></svg></div>
<div class="make" style="left:734px;top:2365px"><svg width="56" height="36"><ellipse cx="28" cy="18" rx="25" ry="15" fill="none" stroke="#ccc" stroke-width="3"/></svg></div>
<div class="make" style="left:858px;top:2365px"><svg width="66" height="24"><rect x="2" y="4" width="62" height="16" fill="none" stroke="#ccc" stroke-width="3"/></svg></div>
<div class="make" style="left:232px;top:2455px"><svg width="46" height="40"><rect x="5" y="2" width="36" height="36" fill="#ccc"/></svg></div>
<div class="make" style="left:358px;top:2455px"><svg width="66" height="36"><ellipse cx="33" cy="18" rx="30" ry="15" fill="none" stroke="#ccc" stroke-width="3"/></svg></div>
<div class="make" style="left:482px;top:2455px"><svg width="56" height="42"><ellipse cx="28" cy="21" rx="25" ry="18" fill="none" stroke="#ccc" stroke-width="3"/></svg></div>
<div class="make" style="left:608px;top:2455px"><svg width="50" height="50"><circle cx="25" cy="25" r="21" fill="none" stroke="#ccc" stroke-width="3"/></svg></div>
<div class="make" style="left:734px;top:2455px"><svg width="46" height="50"><rect x="4" y="3" width="38" height="44" rx="10" fill="none" stroke="#ccc" stroke-width="3"/></svg></div>
<div class="make" style="left:858px;top:2455px"><svg width="50" height="50"><ellipse cx="25" cy="25" rx="22" ry="23" fill="none" stroke="#ccc" stroke-width="3"/></svg></div>
<div class="ph" role="img" aria-label="Car parts arranged in a row: steering wheel, turbo, exhaust pipe, spark plugs, shock absorbers and a wheel rim" style="left:185px;top:2560px;width:845px;height:155px;background:linear-gradient(180deg,rgba(200,200,200,0) 0%,#c9c9c9 60%,#9a9a9a 100%)"></div>
<div class="btn btn-outline-red" style="left:541px;top:2578px;width:118px;height:50px">View All</div>

<!-- footer -->
<div class="abs footer"></div>
<div class="abs logo" style="left:114px;top:2805px"><div class="word">KESTREL</div><div class="sub" style="color:var(--white)">AUTO REPAIR</div></div>
<div class="social" style="left:112px"></div>
<div class="social alt" style="left:154px"></div>
<div class="social alt" style="left:197px"></div>
<div class="social alt" style="left:240px"></div>
<div class="abs" style="left:390px;top:2785px;width:1px;height:175px;background:#444"></div>
<div class="fcol" style="left:432px;color:var(--white)">
  <h5>Quick Links</h5>
  <ul><li class="arrow">Home</li><li class="arrow">About</li><li class="arrow">Services</li><li class="arrow">Blog</li><li>Contact</li></ul>
</div>
<div class="fcol" style="left:639px;color:var(--white)">
  <h5>Our Company</h5>
  <ul><li class="arrow">Terms &amp; Conditions</li><li class="arrow">Privacy Policy</li><li class="arrow">About Us</li><li class="arrow">Support</li></ul>
</div>
<div class="fcol" style="left:864px;color:var(--white)">
  <h5>Contact us</h5>
  <div class="contact-row"><svg width="14" height="20" viewBox="0 0 14 20" style="margin-top:4px"><path d="M7 0a7 7 0 0 0-7 7c0 5 7 13 7 13s7-8 7-13a7 7 0 0 0-7-7z" fill="#fff"/><circle cx="7" cy="7" r="2.5" fill="#0d0d0d"/></svg><span>Lorem ipsum dolor sit<br>amet, consectetur adipiscing</span></div>
  <div class="contact-row"><svg width="16" height="16" viewBox="0 0 16 16" style="margin-top:5px"><path d="M3 1l3 3-2 2c1 2 3 4 5 5l2-2 3 3-2 3C7 15 1 9 1 3z" fill="#fff"/></svg><span>1+ (555) 014 2288</span></div>
  <div class="contact-row"><svg width="16" height="14" viewBox="0 0 16 14" style="margin-top:7px"><rect width="16" height="12" fill="#fff"/><path d="M0 0l8 6 8-6" fill="none" stroke="#0d0d0d" stroke-width="1.4"/></svg><span>hello@kestrelgarage.example</span></div>
</div>
<div class="abs" style="left:112px;top:2985px;width:976px;height:1px;background:#333"></div>
<div class="abs" style="left:432px;top:3020px;color:var(--white);font-size:15px">©Copyrights 2023 Kestrel &nbsp;|&nbsp;&nbsp; All Rights Reserved</div>

</body>
</html>
```